Concreting tools catalogue

I need a catalogue to provide current and potential customers with the item we hold and their prices. THIS WILL HAVE TO BE A FILE THAT I CAN EDIT AS I WILL BE ADDING INFORMATION AND PICTURES. I have provided an example of what I want in the files. Logo to be used is provided in files.

Will be 10 pages approximately excluding front cover and the back.

COVER PAGE:
Underneath VURN put the words "Professional Concrete Equipment"
In the top right corner put "2021". Underneath 2021 put "concrete power equipment and accesories".

BACK PAGE:
Add contact details

The image with two pipes will be use for pages with accesories and will hold a minimum of 2 items.

The third image will be used to display items that we have variations of. A table will be needed at the bottom of the page to display the prices of different variations.

Target Market(s)

concreter workers, industrial

Colors
33b8a4
ffffff

Requirements
Must have
• Please send the catalogue with both white and light grey textured backgorund that looks like concrete. So i can decide on which colour. Please use the green specified in the colours section.

Put sample photos of any 36" power trowels you find on google images.

Select a font suitable for the title of each page and a font used for descriptions.

```html
<!DOCTYPE html>
<html lang="en">
<head>
<meta charset="utf-8">
<title>VURN Catalogue Cover 2021</title>
<link href="https://fonts.googleapis.com/css2?family=Oswald:wght@600;700&family=Work+Sans:wght@400;600&display=swap" rel="stylesheet">
<style>
  :root {
    --teal-deep: #1ea6b6;
    --teal-bright: #35c2d1;
    --paper: #f3f3f3;
    --stage: #dcdcde;
    --ink: #222;
    --white: #ffffff;
  }
  * { box-sizing: border-box; margin: 0; padding: 0; }
  html, body { width: 1200px; height: 840px; overflow: hidden; }
  body {
    background: var(--stage);
    display: flex;
    align-items: center;
    justify-content: center;
    font-family: "Work Sans", Arial, sans-serif;
  }
  .spread { display: flex; width: 1132px; height: 800px; box-shadow: 0 6px 24px rgba(0,0,0,.18); }
  .page { position: relative; width: 566px; height: 800px; overflow: hidden; }

  /* Back cover */
  .back-cover { background: var(--teal-deep); color: var(--white); }
  .back-brand { position: absolute; left: 44px; bottom: 86px; width: 220px; }
  .back-brand .wordmark {
    font-family: "Oswald", Arial, sans-serif; font-weight: 700;
    font-size: 30px; letter-spacing: 4px; line-height: 1; margin-bottom: 8px;
  }
  .back-brand p { font-size: 11px; line-height: 1.35; opacity: .9; }
  .contact { position: absolute; right: 40px; bottom: 64px; font-size: 11px; line-height: 1.4; list-style: none; opacity: .9; }

  /* Front cover */
  .front-cover { background: var(--paper); }
  .year-ribbon { position: absolute; top: 0; right: 0; width: 200px; height: 200px; }
  .wordmark-front {
    position: absolute; left: 44px; top: 150px;
    font-family: "Oswald", Arial, sans-serif; font-weight: 700;
    font-size: 118px; line-height: 1; letter-spacing: 18px; color: var(--teal-bright);
  }
  .headline { position: absolute; left: 44px; right: 0; top: 318px; }
  .headline-line { display: flex; align-items: center; gap: 14px; height: 66px; }
  .headline-line span {
    font-family: "Oswald", Arial, sans-serif; font-weight: 700;
    font-size: 62px; line-height: 1; color: var(--teal-bright); white-space: nowrap;
  }
  .headline-line .bar { flex: 1; height: 44px; background: var(--teal-bright); }
  .products { position: absolute; left: 30px; right: 30px; bottom: 40px; display: flex; justify-content: space-between; align-items: flex-end; }
  .product-photo {
    width: 150px; height: 150px; border-radius: 8px;
    background: radial-gradient(circle at 45% 40%, #ffffff 0%, #e4e4e4 60%, #cfcfcf 100%);
  }
  .product-photo.tall { height: 170px; }
</style>
</head>
<body>
  <div class="spread">
    <section class="page back-cover">
      <div class="back-brand">
        <div class="wordmark">VURN</div>
        <p>Lorem Ipsum is simply dummy text of the printing and typesetting industry.</p>
      </div>
      <ul class="contact">
        <li>T: 000 0000 0000</li>
        <li>E: hello@vurntools.com</li>
        <li>W: vurntools.com</li>
      </ul>
    </section>

    <section class="page front-cover">
      <svg class="year-ribbon" viewBox="0 0 200 200" aria-hidden="false">
        <polygon points="70,0 140,0 200,60 200,130" fill="var(--teal-bright)"/>
        <g transform="translate(128,46) rotate(45)">
          <text x="0" y="0" text-anchor="middle" font-family="Oswald, Arial, sans-serif" font-weight="700" font-size="34" fill="#ffffff">2021</text>
        </g>
        <g transform="translate(112,76) rotate(45)" font-family="Work Sans, Arial, sans-serif" font-size="9.5" fill="#222">
          <text x="0" y="0" text-anchor="middle">concrete power equipment</text>
          <text x="0" y="12" text-anchor="middle">and accesories</text>
        </g>
      </svg>

      <div class="wordmark-front">VURN</div>

      <div class="headline">
        <div class="headline-line"><span>PROFESSIONAL</span><div class="bar"></div></div>
        <div class="headline-line"><span>CONCRETE</span><div class="bar"></div></div>
        <div class="headline-line"><span>EQUIPMENT</span><div class="bar"></div></div>
      </div>

      <div class="products">
        <div class="product-photo" role="img" aria-label="Photo of a white PVC cross pipe fitting"></div>
        <div class="product-photo tall" role="img" aria-label="Photo of a white PVC tee pipe fitting"></div>
        <div class="product-photo" role="img" aria-label="Photo of a white PVC Y-junction pipe fitting"></div>
      </div>
    </section>
  </div>
</body>
</html>
```